Business Card Design for company

We want new business cards. We'd like something different-- yet still highly professional. Our tagline is Providing leadership, delivering success. Stock photos are ok, as long as they are relevant and look upscale.

Target Market(s)

Architecture/Business Management Consulting/Engineering Consulting

Contact Information for Business Card

dark gray background with pops of blue might be good, but you tell me. You're the designers. Rounded corners might be nice, but again, you tell me.

Font styles to use
Serif
Sans Serif

Colors
3276b5
5c5c5c
9d9d9d
fbfbfb

Requirements
Nice to have
• Something different, but still very professional.

```html
<!DOCTYPE html>
<html lang="en">
<head>
<meta charset="utf-8">
<title>Orvane Group – Business Card</title>
<link href="https://fonts.googleapis.com/css2?family=Open+Sans:wght@400;600;700&display=swap" rel="stylesheet">
<style>
  :root {
    --stage: #ececec;
    --card-dark: #212325;
    --card-light: #fbfbfb;
    --brand-blue: #2f66a3;
    --ink: #3f4144;
    --mark-dark: #6b6d70;
    --tagline: #47494c;
  }
  * { box-sizing: border-box; margin: 0; padding: 0; }
  html, body {
    width: 1200px; height: 1000px; overflow: hidden;
    background: var(--stage);
    font-family: "Open Sans", Arial, sans-serif;
  }
  .canvas { position: relative; width: 1200px; height: 1000px; }
  .card {
    position: absolute; left: 266px; width: 666px; height: 396px;
    box-shadow: 0 3px 10px rgba(0,0,0,0.18);
  }
  .card--front { top: 75px; background: var(--card-dark); }
  .card--back { top: 534px; background: var(--card-light); }

  .front-mark {
    position: absolute; left: 0; right: 0; top: 155px;
    text-align: center;
    font-weight: 600; font-size: 66px; letter-spacing: 1px;
    color: var(--mark-dark);
  }
  .front-tagline {
    position: absolute; left: 0; right: 0; top: 347px;
    text-align: center; font-size: 16px; color: var(--tagline);
  }
  .front-tagline .sep { margin: 0 10px; }

  .back-mark {
    position: absolute; left: 52px; top: 78px;
    font-weight: 600; font-size: 40px; color: var(--ink);
  }
  .contact { position: absolute; left: 53px; top: 266px; font-size: 16px; color: var(--ink); }
  .contact p { line-height: 28px; white-space: nowrap; }
  .contact .title-line { margin-bottom: 3px; }
  .contact .name,
  .contact .label { font-weight: 700; color: var(--brand-blue); }
  .contact .sep { color: var(--brand-blue); margin: 0 8px; }
  .contact .sep--tight { margin: 0 3px; }
  .contact .domain { font-weight: 600; color: var(--brand-blue); }
</style>
</head>
<body>
<main class="canvas">
  <section class="card card--front">
    <div class="front-mark">Orvane Group</div>
    <p class="front-tagline">Guiding Direction<span class="sep">|</span>Building Results</p>
  </section>

  <section class="card card--back">
    <div class="back-mark">Orvane Group</div>
    <div class="contact">
      <p class="title-line"><span class="name">DORIAN HALE</span><span class="sep sep--tight">|</span>Managing Director</p>
      <p><span class="label">p.</span> 555 010 2400 &nbsp; <span class="label">c.</span> 555 010 7730 <span class="sep">|</span> info@orvanegroup.com</p>
      <p>www.<span class="domain">orvanegroup</span>.com <span class="sep">|</span> 18 Marlow Ave, Fairview TX 75069</p>
    </div>
  </section>
</main>
</body>
</html>
```